Book cover

I am working with my publisher to publish my book They came up with a book cover but I don't like it. I want to see different designs. The book Title is Shiftcraftery the subtitle How to Steer Upheaval with Focus, Poise & Resolve by Marilyn T. Hargreave
I want to use my Brand Colors including the blue. I am uploading the covers of my other book. This is a professional leadership book. The publisher will make the cover when providing them a new design. the Shiftcraftery one is one I played with on Canva. I would like more color and to incorporate the blue. I want a spot at the top where I can write a quote. Shiftcraftery is one word in the text so should be the same on the cover. I want the cover to show energy movement and am open to an image too. I am attaching logos for the feel of the brand and brand rgb codes.

```html
<!DOCTYPE html>
<html lang="en">
<head>
<meta charset="UTF-8">
<title>Shiftcraftery — Book Cover</title>
<link rel="stylesheet" href="https://fonts.googleapis.com/css2?family=Bebas+Neue&family=Montserrat:wght@300;500;600&family=Alegreya:wght@800&display=swap">
<style>
  :root {
    --navy: #27303d;
    --teal-deep: #1d5f67;
    --teal-mid: #3c8e92;
    --green: #2e9a67;
    --cream: #ebe6da;
    --paper: #eeeee8;
    --title-white: #f4f2ec;
    --accent-red: #e0332a;
    --band-red: #e2231a;
    --band-orange: #f08a48;
    --author-teal: #1f8a90;
  }
  html, body {
    margin: 0;
    padding: 0;
    width: 980px;
    height: 1200px;
    overflow: hidden;
    background: var(--paper);
  }
  .cover {
    position: relative;
    width: 980px;
    height: 1200px;
    overflow: hidden;
    background: var(--paper);
  }
  .cover-photo {
    position: absolute;
    left: 0;
    top: 0;
    width: 980px;
    height: 1017px;
    background:
      radial-gradient(ellipse 260px 520px at 800px 260px, rgba(235,230,218,0.95), rgba(235,230,218,0) 70%),
      radial-gradient(ellipse 380px 70px at 420px 520px, rgba(46,154,103,0.95), rgba(46,154,103,0) 75%),
      radial-gradient(ellipse 120px 260px at 430px 420px, rgba(176,86,70,0.7), rgba(176,86,70,0) 75%),
      radial-gradient(ellipse 140px 420px at 720px 560px, rgba(230,92,50,0.55), rgba(230,92,50,0) 75%),
      linear-gradient(180deg, rgba(39,48,61,0) 60%, rgba(29,95,103,0.9) 100%),
      linear-gradient(90deg, var(--navy) 0%, #3a4450 45%, #c9c3b4 80%, var(--cream) 100%);
  }
  .tagline {
    position: absolute;
    left: 84px;
    top: 236px;
    margin: 0;
    font-family: "Montserrat", sans-serif;
    font-weight: 600;
    font-size: 16.5px;
    line-height: 21px;
    letter-spacing: 0.2px;
    color: var(--title-white);
    text-transform: uppercase;
  }
  .title {
    position: absolute;
    left: 78px;
    top: 284px;
    width: 860px;
    height: 180px;
  }
  .title text {
    font-family: "Bebas Neue", sans-serif;
    font-size: 232px;
  }
  .title .word-lead { fill: var(--title-white); }
  .title .word-tail { fill: var(--accent-red); }
  .subtitle-band {
    position: absolute;
    left: 0;
    top: 608px;
    width: 980px;
    height: 132px;
    background: linear-gradient(90deg, var(--band-red) 0%, var(--band-red) 55%, var(--band-orange) 100%);
    display: flex;
    flex-direction: column;
    align-items: center;
    justify-content: center;
    color: #fff;
    font-family: "Montserrat", sans-serif;
  }
  .subtitle-band .lead {
    font-weight: 300;
    font-size: 28px;
    line-height: 36px;
    letter-spacing: 0.5px;
  }
  .subtitle-band .pillars {
    font-weight: 500;
    font-size: 29px;
    line-height: 36px;
    letter-spacing: 1px;
    text-transform: uppercase;
  }
  .author-strip {
    position: absolute;
    left: 0;
    top: 1017px;
    width: 980px;
    height: 183px;
    background: var(--paper);
    display: flex;
    align-items: center;
    justify-content: center;
  }
  .author-name {
    margin: 0;
    font-family: "Alegreya", serif;
    font-weight: 800;
    font-size: 50px;
    color: var(--author-teal);
  }
</style>
</head>
<body>
  <main class="cover">
    <div class="cover-photo" role="img" aria-label="Motion-blurred photograph of a person striding through a bright corridor, in navy, green, teal and cream tones"></div>

    <p class="tagline">Shiftcraftery is the essential playbook<br>to turn your uncertainty into possibility</p>

    <svg class="title" viewBox="0 0 860 180" aria-label="Shiftcraftery">
      <text x="0" y="176" textLength="856" lengthAdjust="spacingAndGlyphs"><tspan class="word-lead">SHIFT</tspan><tspan class="word-tail">CRAFTERY</tspan></text>
    </svg>

    <div class="subtitle-band">
      <span class="lead">How to Steer Upheaval with</span>
      <span class="pillars">Focus, Poise &amp; Resolve</span>
    </div>

    <div class="author-strip">
      <p class="author-name">Marilyn T. Hargreave</p>
    </div>
  </main>
</body>
</html>
```